House flipping business web site needed

birchstoneholdings.example.
I am a residential developer in Northern NJ and I am looking for a fresh new updated website. I have an intro video about my company being made now. I don't update it very often but I want an easy format that I can add update photos to on projects I have worked on or homes I renovate for sale.

Target Market(s)

investors into my projects so a portfolio , people looking to sell their homes to me.

Industry/Entity Type

Real Estate Development

Number of Pages Required

4 page

Font styles to use
Serif

Colors
33b8a4
39a9d7
cadf82

Requirements
Must have
• space for an intro video about my company
• a portfolio with pictures and information about each project
• Markets we serve- Morris County, NJ
• My logo- already created
• SEO
• Yes I would like this to function over all platforms. Phone, computer, all platforms.
• history and background page
• I am looking for a completed page that I can upload to the site that hosts my website
Nice to have
• I want something creative, easy to navigate. modern.

```html
<!DOCTYPE html>
<html lang="en">
<head>
<meta charset="utf-8">
<title>Birchstone Holdings – Homes for Sale and Rent</title>
<link rel="stylesheet" href="https://fonts.googleapis.com/css2?family=Raleway:wght@400;500;600;700&family=Open+Sans:wght@400;600;700&family=Parisienne&display=swap">
<style>
:root{
  --blue:#39a9d7;
  --blue-dark:#2b95c2;
  --ink:#1e1e1e;
  --text:#333;
  --muted:#777;
  --footer:#f0f0f0;
  --footer-bar:#ffffff;
}
*{box-sizing:border-box;margin:0;padding:0}
html,body{width:1200px;height:3390px;overflow:hidden}
body{position:relative;background:#fff;font-family:"Open Sans",Arial,sans-serif;color:var(--text)}
.abs{position:absolute}

/* Hero */
.hero{left:0;top:0;width:1200px;height:675px;background:linear-gradient(180deg,#6f8fb0 0%,#9a6a44 35%,#7a4e30 60%,#4d6a2e 85%,#3e5a26 100%)}
.logo-box{left:61px;top:27px;width:339px;height:319px;background:#fff;display:flex;flex-direction:column;align-items:center;justify-content:center;gap:18px}
.logo-mark{width:120px;height:120px;border-radius:50%;background:var(--blue)}
.logo-name{font-family:"Raleway",sans-serif;font-weight:700;color:var(--blue-dark);font-size:32px;letter-spacing:2px;text-align:center;line-height:1.15}
.menu-btn{left:1078px;top:145px;width:59px;height:49px;background:#111;border-radius:4px}
.menu-btn span{position:absolute;left:13px;width:33px;height:3px;background:#fff}
.caption{left:199px;top:423px;width:802px;height:165px;background:rgba(57,169,215,.88);text-align:center;color:#fff;padding:26px 30px}
.caption h1{font-family:"Parisienne",cursive;font-weight:400;font-size:36px;line-height:1.1;margin-bottom:16px;white-space:nowrap}
.caption p{font-size:12.5px;line-height:2.1}
.arrow{top:615px;width:45px;height:45px;background:#111;display:flex;align-items:center;justify-content:center}

/* Headings */
.section-title{left:0;width:1200px;text-align:center;font-family:"Raleway",sans-serif;font-weight:600;color:var(--blue);font-size:42px}
.about-sub{left:0;top:814px;width:1200px;text-align:center;font-weight:600;font-size:19px;color:var(--ink)}
.about-text{left:151px;top:852px;width:898px;text-align:center;font-size:13.5px;line-height:2.05;color:#333}

/* Listing grid */
.tile{overflow:hidden}
.featured{left:463px;top:1105px;width:676px;height:504px;background:linear-gradient(180deg,#2a2c2e 0%,#3b3a36 55%,#1c1f22 100%);text-align:center;color:#fff}
.featured h3{margin-top:192px;font-family:"Open Sans",sans-serif;font-weight:600;font-size:24px}
.featured .loc{font-size:13px;color:#bbb;margin-top:6px}
.featured .price{font-weight:600;font-size:18px;color:var(--blue);margin-top:6px}
.featured .open{display:inline-block;margin-top:16px;background:var(--blue);color:#fff;font-size:11px;padding:9px 20px}
.btn-view{left:522px;top:1923px;width:156px;height:48px;background:var(--blue);color:#fff;font-size:19px;display:flex;align-items:center;justify-content:center}

/* Video band */
.band{left:0;top:2032px;width:1200px;height:538px;background:linear-gradient(180deg,#35373b,#23262a)}
.band-title{left:61px;top:2062px;font-family:"Raleway",sans-serif;font-weight:700;color:#fff;font-size:21px;text-transform:uppercase}
.video{left:61px;top:2118px;width:669px;height:422px;background:linear-gradient(180deg,#dfe7ee 0%,#c9d3da 45%,#5d7d4a 75%,#3f5e32 100%);border:4px solid #fff}
.video-bar{position:absolute;left:0;bottom:0;width:100%;height:34px;background:rgba(0,0,0,.85)}
.video-play{position:absolute;left:50%;top:50%;width:64px;height:64px;margin:-32px 0 0 -32px;border-radius:50%;background:rgba(0,0,0,.6)}
.quote{left:820px;top:2032px;width:319px;height:538px;background:#3a3c40}
.quote-head{position:absolute;left:0;top:0;width:319px;height:172px}
.quote-head p{position:absolute;left:0;top:44px;width:319px;text-align:center;color:#fff;font-family:"Raleway",sans-serif;font-weight:700;font-size:20px;line-height:1.3;text-transform:uppercase}
.field{left:866px;width:232px;height:40px;background:#fff;border:1px solid #aaa;font-size:11px;color:#777;padding:12px 6px}
.send{left:866px;top:2502px;width:232px;height:41px;background:var(--blue);color:#fff;font-weight:600;font-size:15px;display:flex;align-items:center;justify-content:center}

/* Steps */
.steps-title{left:0;top:2650px;width:1200px;text-align:center;font-family:"Raleway",sans-serif;font-weight:600;font-size:40px;color:var(--ink)}
.steps-sub{left:0;top:2716px;width:1200px;text-align:center;font-size:14px;color:#333}
.step{top:2796px;width:112px;height:112px;border-radius:50%;background:var(--blue);display:flex;align-items:center;justify-content:center}
.dots{top:2849px;width:120px;height:6px;background:radial-gradient(circle,#111 2.5px,transparent 3px) 0 0/17px 6px repeat-x}
.search{left:321px;top:2954px;width:459px;height:38px;border:1px solid #999;background:#fff}
.submit{left:780px;top:2954px;width:101px;height:38px;background:#111;color:#fff;font-weight:600;font-size:15px;display:flex;align-items:center;justify-content:center}

/* Footer */
.footer{left:0;top:3058px;width:1200px;height:282px;background:var(--footer)}
.foot-title{top:3108px;font-family:"Raleway",sans-serif;font-size:19px;color:#222;text-transform:uppercase}
.foot-sub{font-family:"Raleway",sans-serif;font-weight:700;font-size:12.5px;color:#222;text-transform:uppercase}
.foot-line{font-size:12.5px;color:#333;line-height:1.5}
.foot-list{list-style:none;font-size:12.5px;color:#333}
.foot-list li{line-height:27px}
.foot-list li::before{content:"•";margin-right:8px}
.news-input{left:884px;top:3214px;width:198px;height:38px;background:#fff;border:1px solid #ccc;font-size:12px;padding:10px 8px;color:#444}
.news-btn{left:1082px;top:3214px;width:56px;height:38px;background:var(--blue);display:flex;align-items:center;justify-content:center}
.social{top:3275px;width:12px;height:12px;border-radius:50%;background:#bbb}
.bottom-bar{left:0;top:3340px;width:1200px;height:50px;background:var(--footer-bar);font-size:11.5px;color:#444}
.bottom-bar .copy{position:absolute;left:61px;top:18px}
.bottom-bar .links{position:absolute;right:61px;top:18px;display:flex;gap:24px}
</style>
</head>
<body>

<!-- Hero -->
<section class="abs hero" role="img" aria-label="Photo of a cedar-shingled lakeside house among autumn trees"></section>
<div class="abs logo-box">
  <div class="logo-mark"></div>
  <div class="logo-name">BIRCHSTONE<br>HOLDINGS</div>
</div>
<div class="abs menu-btn"><span style="top:14px"></span><span style="top:23px"></span><span style="top:32px"></span></div>
<div class="abs caption">
  <h1>Find your perfect New Home and start a new life!</h1>
  <p>Renovated homes across Morris County, ready for families to move in and enjoy.<br>Browse current listings, book a visit and let our team guide you home.</p>
</div>
<div class="abs arrow" style="left:540px"><svg width="14" height="20" viewBox="0 0 14 20"><path d="M11 2 3 10l8 8" fill="none" stroke="#fff" stroke-width="2.5"/></svg></div>
<div class="abs arrow" style="left:612px"><svg width="14" height="20" viewBox="0 0 14 20"><path d="m3 2 8 8-8 8" fill="none" stroke="#fff" stroke-width="2.5"/></svg></div>

<!-- About -->
<h2 class="abs section-title" style="top:732px">About Birchstone Holdings</h2>
<div class="abs about-sub">What we do</div>
<p class="abs about-text">We are a team of experienced home buyers and renovators in the Morris County, NJ area. Our specialty is purchasing distressed homes and property. We then collaborate with the best talents in Northern New Jersey to renovate those properties and transform them into the best house in the neighborhood. As a result we create equity, a return on investment and most importantly we give home buyers a worry free property that provides a better way of life and hope for their future.</p>

<!-- Listings -->
<h2 class="abs section-title" style="top:1024px;font-size:40px">Birchstone for Sale and Rent</h2>
<div class="abs tile" style="left:61px;top:1105px;width:373px;height:237px;background:linear-gradient(160deg,#8fb0c8,#7b5a3c 60%,#4b3a2a)" role="img" aria-label="Wooden deck overlooking a mountain"></div>
<div class="abs tile" style="left:61px;top:1372px;width:373px;height:237px;background:linear-gradient(170deg,#8cbad6,#5f8a4c 55%,#6a3e2c)" role="img" aria-label="Patio with chairs above a wooded valley"></div>
<div class="abs featured" role="img" aria-label="Lakeside lodge at dusk with kayaks on the shore">
  <h3>259 Birch Hollow Lane</h3>
  <div class="loc">United States / New Jersey</div>
  <div class="price">$199,000</div>
  <div class="open">OPEN HOUSE</div>
</div>
<div class="abs tile" style="left:61px;top:1638px;width:373px;height:238px;background:linear-gradient(180deg,#6fa3c9,#b9c8cf 50%,#3d6e8a)" role="img" aria-label="Boathouse on a calm lake at sunset"></div>
<div class="abs tile" style="left:463px;top:1638px;width:323px;height:238px;background:linear-gradient(180deg,#c9d6cf,#7ea28a 55%,#3f6a6a)" role="img" aria-label="Pavilion on a misty lake shore"></div>
<div class="abs tile" style="left:816px;top:1638px;width:323px;height:238px;background:linear-gradient(180deg,#2d3b4a,#4a4a3c 50%,#c49a52 70%,#1f2b33)" role="img" aria-label="Lit lake house with dock in the evening"></div>
<div class="abs btn-view">View all</div>

<!-- Video band -->
<section class="abs band" role="img" aria-label="Dimmed photo of a lake house at night"></section>
<div class="abs band-title">Take a brief tour of our facility</div>
<div class="abs video" role="img" aria-label="Company intro video showing a modern white house">
  <div class="video-play"><svg width="64" height="64" viewBox="0 0 64 64"><path d="M26 20v24l19-12z" fill="#fff"/></svg></div>
  <div class="video-bar"></div>
</div>
<div class="abs quote">
  <svg class="quote-head" width="319" height="172" viewBox="0 0 319 172"><path d="M0 0h319v128l-159.5 44L0 128z" fill="#39a9d7"/></svg>
  <div class="quote-head"><p>Get in touch contact<br>us for a quote</p></div>
</div>
<div class="abs field" style="top:2236px">*Name</div>
<div class="abs field" style="top:2286px">*Last Name</div>
<div class="abs field" style="top:2338px">*Your Email</div>
<div class="abs field" style="top:2391px;height:97px">*Message</div>
<div class="abs send">Send Question</div>

<!-- Steps -->
<h2 class="abs steps-title">Get Started With Your Sweet Home Search Now</h2>
<p class="abs steps-sub">Fair cash offers, honest guidance and a quick, stress-free closing.</p>
<div class="abs step" style="left:254px"><svg width="50" height="50" viewBox="0 0 50 50"><circle cx="21" cy="21" r="13" fill="none" stroke="#fff" stroke-width="4"/><path d="m31 31 12 12" stroke="#fff" stroke-width="6" stroke-linecap="round"/></svg></div>
<div class="abs dots" style="left:382px"></div>
<div class="abs step" style="left:538px"><svg width="46" height="46" viewBox="0 0 46 46"><path d="M10 4c3 0 5 7 5 9s-4 3-4 5c2 6 6 10 12 12 2 0 3-4 5-4s9 2 9 5-3 8-8 8C18 39 7 28 4 15c0-5 3-11 6-11z" fill="none" stroke="#fff" stroke-width="3"/></svg></div>
<div class="abs dots" style="left:667px"></div>
<div class="abs step" style="left:816px"><svg width="48" height="48" viewBox="0 0 48 48"><circle cx="16" cy="16" r="10" fill="none" stroke="#fff" stroke-width="4"/><path d="m23 23 18 18m-6-6 5-5m-9 1 4-4" stroke="#fff" stroke-width="4" stroke-linecap="round"/></svg></div>
<div class="abs search"></div>
<div class="abs submit">Submit</div>

<!-- Footer -->
<footer class="abs footer"></footer>
<div class="abs foot-title" style="left:61px">Contact Us</div>
<svg class="abs" style="left:61px;top:3163px" width="14" height="16" viewBox="0 0 14 16"><path d="M1 7 7 2l6 5v8H1z" fill="none" stroke="#666" stroke-width="1.3"/></svg>
<div class="abs foot-line" style="left:88px;top:3160px">48 Larchmont Way<br>Denville NJ 07834</div>
<svg class="abs" style="left:62px;top:3217px" width="12" height="16" viewBox="0 0 12 16"><rect x="1" y="1" width="10" height="14" rx="2" fill="none" stroke="#666" stroke-width="1.3"/></svg>
<div class="abs foot-line" style="left:88px;top:3217px">+1 (973) 555 0148</div>
<svg class="abs" style="left:61px;top:3264px" width="16" height="12" viewBox="0 0 16 12"><rect x="1" y="1" width="14" height="10" fill="none" stroke="#666" stroke-width="1.3"/><path d="m1 1 7 6 7-6" fill="none" stroke="#666" stroke-width="1.3"/></svg>
<div class="abs foot-line" style="left:88px;top:3261px">info@birchstoneholdings.example</div>

<div class="abs foot-title" style="left:366px">Services</div>
<ul class="abs foot-list" style="left:366px;top:3150px">
  <li>About Us</li><li>Portfolio</li><li>Sell Your Home</li><li>Investors</li><li>Privacy Policy</li>
</ul>

<div class="abs foot-title" style="left:579px">Markets We Serve</div>
<ul class="abs foot-list" style="left:579px;top:3150px">
  <li>Morris County, NJ</li><li>Northern New Jersey</li>
</ul>
<div class="abs foot-sub" style="left:579px;top:3220px">Project Types</div>
<ul class="abs foot-list" style="left:579px;top:3238px">
  <li>Renovations &amp; Flips</li><li>Rentals</li>
</ul>

<div class="abs foot-title" style="left:884px">Newsletter !</div>
<div class="abs foot-line" style="left:884px;top:3152px;width:255px;line-height:1.9">Sign up for our newsletter and see new listings and project updates first.</div>
<div class="abs news-input">Enter your email here*</div>
<div class="abs news-btn"><svg width="18" height="12" viewBox="0 0 18 12"><path d="M1 6h15m-5-5 5 5-5 5" fill="none" stroke="#fff" stroke-width="2"/></svg></div>
<div class="abs social" style="left:884px"></div>
<div class="abs social" style="left:906px"></div>
<div class="abs social" style="left:928px"></div>
<div class="abs social" style="left:950px"></div>
<div class="abs social" style="left:972px"></div>

<div class="abs bottom-bar">
  <div class="copy">Copyright 2016 ~ Birchstone Holdings. ~All rights reserved.</div>
  <div class="links"><span>Privacy &amp; Cookies</span><span>Terms &amp; Conditions</span><span>About Us</span><span>Contact Us</span></div>
</div>

</body>
</html>
```